This is a label for a new sake made in Japan imported into Aust

This will be a bottle label for a new sake imported into Australia. The hero of the label is the Velmora. We have joined the "O" meaning great in Japanese and used sake with "Z" to have Velmora with the play on words using Oz as in our slang for Aussie. A modern label with a Japanese take is key. This is a premium sake made in Japan for the Australian market.
The "Tall Casks" up the top is the name of the company, we have yet to design a logo for the company.

Target Market(s)

Alcohol

Logo Text

Velmora

Font styles to use
Serif

Requirements
Must have
• easy to read, with a hint of Japanese origin
Should not have
• too busy

```html
<!DOCTYPE html>
<html lang="en">
<head>
<meta charset="utf-8">
<title>Velmora – Premium Japanese Sake Label</title>
<link href="https://fonts.googleapis.com/css2?family=Josefin+Sans:wght@200&family=Playfair+Display:wght@400;700&family=Montserrat:wght@600&display=swap" rel="stylesheet">
<style>
  :root {
    --backdrop: #ececec;
    --label-white: #ffffff;
    --ink: #2a2a2a;
    --sake-red: #b3202c;
    --band-black: #161616;
    --band-grey-top: #3a3a3a;
    --band-grey-bottom: #6d6d6d;
    --band-text: #d4d4d4;
  }
  * { margin: 0; padding: 0; box-sizing: border-box; }
  html, body {
    width: 1155px;
    height: 1200px;
    overflow: hidden;
    background: var(--backdrop);
  }
  .canvas {
    position: relative;
    width: 1155px;
    height: 1200px;
  }
  .label {
    position: absolute;
    left: 77px;
    top: 47px;
    width: 1000px;
    height: 1105px;
    background: var(--label-white);
    box-shadow: 0 4px 18px rgba(0,0,0,0.08);
  }
  .company-name {
    position: absolute;
    left: 240px;
    top: 92px;
    width: 500px;
    text-align: center;
    font-family: "Josefin Sans", sans-serif;
    font-weight: 200;
    font-size: 80px;
    letter-spacing: 4px;
    color: var(--ink);
    line-height: 1;
  }
  .abv-panel {
    position: absolute;
    left: 845px;
    top: 53px;
    width: 131px;
    height: 402px;
    border: 4px solid var(--sake-red);
    padding: 7px;
  }
  .abv-inner {
    width: 100%;
    height: 100%;
    border: 2px solid var(--sake-red);
    display: flex;
    flex-direction: column;
  }
  .abv-cell {
    flex: 1;
    display: flex;
    flex-direction: column;
    justify-content: center;
    align-items: center;
    font-family: "Playfair Display", serif;
    font-size: 30px;
    line-height: 1.5;
    color: var(--ink);
  }
  .abv-cell + .abv-cell {
    border-top: 2px dotted var(--sake-red);
  }
  .brand-lockup {
    position: absolute;
    left: 50px;
    top: 560px;
    width: 920px;
    display: flex;
    align-items: center;
    gap: 36px;
  }
  .brand-dot {
    flex: none;
    width: 90px;
    height: 90px;
    border-radius: 50%;
    background: var(--sake-red);
  }
  .brand-name {
    font-family: "Playfair Display", serif;
    font-weight: 700;
    font-size: 190px;
    line-height: 1;
    color: var(--ink);
    letter-spacing: 2px;
  }
  .band {
    position: absolute;
    left: 0;
    top: 905px;
    width: 1000px;
    height: 200px;
  }
  .band-stripe {
    height: 62px;
    background: var(--band-black);
  }
  .band-base {
    height: 138px;
    background: linear-gradient(to bottom, var(--band-grey-top), var(--band-grey-bottom));
    display: flex;
    align-items: center;
    justify-content: center;
  }
  .band-tagline {
    font-family: "Montserrat", sans-serif;
    font-weight: 600;
    font-size: 38px;
    letter-spacing: 6px;
    color: var(--band-text);
  }
</style>
</head>
<body>
  <div class="canvas">
    <section class="label">
      <div class="company-name">TALL CASKS</div>

      <div class="abv-panel">
        <div class="abv-inner">
          <div class="abv-cell"><span>ALC</span><span>16%</span></div>
          <div class="abv-cell"><span>VOL</span><span>720 ml</span></div>
        </div>
      </div>

      <div class="brand-lockup">
        <div class="brand-dot"></div>
        <div class="brand-name">Velmora</div>
      </div>

      <div class="band">
        <div class="band-stripe"></div>
        <div class="band-base">
          <span class="band-tagline">PREMIUM JAPANESSE SAKE</span>
        </div>
      </div>
    </section>
  </div>
</body>
</html>
```